WP website design (Dorlen Group)

We need a wordpress design for an established auction and real estate company based in Kansas. The winning design will incorporate a professional color scheme with company logo in a clean layout with specified widgets. The design needs to consider that this will be developed on a responsive theme. Colors are blue and gray, with perhaps black or other as an accent/highlight color.

Must Have:
- Navigation:
1) Home 2) Auctions 3) Real Estate Listings 4) Rentals 5) Our Team 6) Services 7) Past Auctions 8) Testimonials 9) Contact Us

Page will have large slideshow, please use either image provided as the initial slide. Homepage will have auctions - as at http://brindlebidhouse.com/upcoming-auctions/. Home page will also have 2 calls to action: "NOTIFY ME OF UPCOMING AUCTIONS" (newsletter signup), and "I AM READY TO SELL. PLEASE CONTACT ME FOR A FREE CONSULTATION." with an email button.

Footer will have smaller company logo, credit card logo, and attached association logos and this contact info:
.(555) 318-7061: OFFICE
(555) 318-7095: FAX
dgroup@vrbx.com: email
Address: 718 N. Elm Ave., Johnson KS
Mailing Address: PO Box 927, Johnson, KS

Widgets:
1) email sign up 2) Social media (twitter, FB, linked-in, pinterest) 3) Mortgage calculator 4) testimonials blog

Nice to Have:
- demonstrate the drop-down menu styling, e.g. under Auctions
Auction Calendar
4 Key Auction Methods
Auction Benefits

Industry/Entity Type

Real Estate

Font styles to use
Sans Serif

Colors

Designer to choose colors to be used in the design.

Requirements
Must have
• - Navigation:

.(555) 318-7061: OFFICE
(555) 318-7095: FAX
dgroup@vrbx.com: email

Widgets:
Nice to have
• Nice to Have:
Auction Calendar
4 Key Auction Methods
Auction Benefits

```html
<!DOCTYPE html>
<html lang="en">
<head>
<meta charset="utf-8">
<title>Dorlen Group — Auctions &amp; Real Estate</title>
<link rel="stylesheet" href="https://fonts.googleapis.com/css2?family=Open+Sans:ital,wght@0,400;0,600;0,700;1,400&family=Marcellus&display=swap">
<style>
:root{
  --blue:#3b3bcc;
  --blue-dark:#2626a0;
  --blue-text:#2e2ea8;
  --red:#a3181d;
  --yellow:#f2ea1c;
  --ink:#333;
  --muted:#777;
  --rule:#e1e1e1;
  --panel:#323232;
  --footer:#2b2b2b;
  --footer-deep:#1e1e1e;
  --light:#f2f2f2;
}
*{box-sizing:border-box;margin:0;padding:0}
html,body{width:1200px;height:2821px;overflow:hidden;background:#fff}
body{position:relative;font-family:"Open Sans",Arial,sans-serif;color:var(--ink)}
.abs{position:absolute}
.serif{font-family:"Marcellus",Georgia,serif}

/* header */
.brand{left:100px;top:30px;display:flex;align-items:center;gap:10px;font-family:"Marcellus",Georgia,serif;font-size:30px;color:var(--blue-dark)}
.brand-mark{width:26px;height:26px;border-radius:50%;background:var(--blue-dark)}
.search{left:899px;top:40px;width:200px;height:35px;background:#efefef;border-radius:3px;font-size:12px;color:#999;padding:10px 14px}
.search svg{position:absolute;right:10px;top:9px}
.nav{left:0;top:115px;width:1200px;height:51px;background:linear-gradient(#4848d6,#3434c2)}
.nav ul{position:absolute;left:100px;top:0;width:1000px;height:51px;display:flex;list-style:none;border-left:1px solid #2a2aa0}
.nav li{flex:none;height:51px;line-height:51px;color:#fff;font-size:14px;font-weight:600;text-align:center;white-space:nowrap;border-right:1px solid #2a2aa0}
.nav li.active{background:var(--blue-dark)}

/* hero */
.hero{left:0;top:166px;width:1200px;height:460px;background:linear-gradient(#c9c4d0 0%,#e8d3c4 22%,#7a8a55 32%,#4f6a2a 60%,#3c5520 100%)}
.hero-arrow{top:359px;width:62px;height:78px;background:rgba(0,0,0,.55)}
.hero-caption{left:0;top:562px;width:1200px;text-align:center;color:#fff;font-size:27px;letter-spacing:.5px}

/* intro */
.intro-title{left:100px;top:666px;width:1000px;text-align:center;color:var(--blue-text);font-size:23px;font-weight:700}
.intro-copy{left:150px;top:705px;width:900px;text-align:center;font-size:14.5px;line-height:23.5px;color:var(--muted)}
.divider{left:100px;top:815px;width:1000px;height:1px;background:var(--rule)}

/* auctions */
.section-title{left:100px;top:854px;font-size:20px;color:var(--blue-text)}
.more-dot{left:816px;top:857px;width:18px;height:18px;border-radius:50%;background:#c9c9c9}
.card{left:100px;width:737px;height:411px}
.card .photo{position:absolute;left:2px;top:0;width:385px;height:197px}
.card .thumb{position:absolute;top:203px;width:124px;height:77px}
.card .loc{position:absolute;left:2px;top:287px;width:385px;height:47px;background:#e6e6e6;font-size:14px;color:#444;padding:14px 0 0 48px;white-space:nowrap}
.card .loc svg{position:absolute;left:12px;top:10px}
.card .info{position:absolute;left:402px;top:0;width:335px}
.card h3{font-size:19px;font-weight:400;color:var(--red);margin-top:-2px;white-space:nowrap}
.card .desc{font-size:13px;line-height:20.5px;color:var(--muted);margin-top:4px;height:111px;border-bottom:1px solid var(--rule)}
.card .mode{font-size:18px;color:#333;margin-top:14px}
.card .when{font-size:12.5px;line-height:28px;color:#444;white-space:nowrap}
.card .when b{display:inline-block;width:52px;font-weight:600}
.card .sub{border-bottom:1px solid var(--rule);padding-bottom:6px}
.card .actions{position:absolute;left:0;top:349px;width:737px;height:56px;display:flex;align-items:center;font-size:16.5px;color:#333;border-top:1px solid var(--rule)}
.card .actions span{flex:none;display:flex;align-items:center;gap:12px;padding-left:22px;border-right:1px solid var(--rule);height:30px;white-space:nowrap}
.card .actions span:nth-child(1){width:126px;padding-left:14px}
.card .actions span:nth-child(2){width:150px}
.card .actions span:nth-child(3){width:160px}
.card .actions span:nth-child(4){width:301px;border-right:0}
.card .base{position:absolute;left:0;top:404px;width:737px;height:7px;background:#d2d2d2}

/* sidebar */
.box{left:856px;width:244px;color:#fff;padding:18px 19px}
.box h4{font-family:"Marcellus",Georgia,serif;font-size:17.5px;line-height:24px;font-weight:400;letter-spacing:.3px}
.notify{top:861px;height:164px;background:var(--blue)}
.field{background:#fff;color:#999;font-size:12px;height:36px;border-radius:2px;padding:10px 14px;margin-top:12px}
.btn{display:inline-block;background:var(--yellow);color:#222;font-size:13px;font-weight:600;padding:6px 12px;border-radius:2px}
.sell{top:1040px;height:168px;background:var(--blue)}
.mortgage{top:1225px;height:352px;background:var(--panel)}
.mortgage h4{padding-left:40px;position:relative}
.mortgage h4 svg{position:absolute;left:0;top:4px}
.mortgage label{display:block;font-size:12.5px;margin-top:14px}
.mortgage .field{margin-top:6px}

/* testimonials */
.testimonials{left:0;top:2299px;width:1200px;height:259px;background:var(--light)}
.testimonials h2{position:absolute;left:0;top:36px;width:1200px;text-align:center;font-size:31px;font-weight:400;color:var(--blue-text)}
.avatar{left:123px;top:2394px;width:130px;height:130px;border-radius:50%;background:linear-gradient(#d9d2cc,#b3a397);border:5px solid #fff;box-shadow:0 2px 6px rgba(0,0,0,.25)}
.quote{left:273px;top:2407px;width:800px;font-size:14.5px;font-style:italic;line-height:24px;color:#555}
.quote cite{display:block;font-style:normal;font-weight:600;color:#222;margin-top:8px;font-size:14.5px}
.t-arrow{top:2410px}

/* footer */
.footer{left:0;top:2558px;width:1200px;height:211px;background:var(--footer)}
.f-brand{left:126px;top:2600px;font-family:"Marcellus",Georgia,serif;font-size:27px;color:#fff;display:flex;align-items:center;gap:10px;white-space:nowrap}
.f-brand i{width:22px;height:22px;border-radius:50%;background:#fff;display:block}
.badge{top:2592px;height:55px;background:#f4f4f4;border-radius:2px}
.vline{top:2585px;width:1px;height:70px;background:#555}
.pay{top:2600px;width:58px;height:37px;background:#e9e9e9;border-radius:3px}
.social{top:2603px;width:30px;height:30px;border-radius:50%;background:#6f6f8f}
.f-rule{left:100px;top:2680px;width:1000px;height:1px;background:#444}
.contact{top:2704px;font-size:13px;line-height:22px;color:#9a9a9a;white-space:nowrap}
.contact svg{position:absolute;left:-30px;top:6px}
.copyright{left:0;top:2769px;width:1200px;height:52px;background:var(--footer-deep);text-align:center;color:#888;font-size:13px;line-height:52px}
</style>
</head>
<body>

<header>
  <div class="abs brand"><span class="brand-mark"></span>Dorlen Group</div>
  <div class="abs search">Search
    <svg width="16" height="16" viewBox="0 0 16 16"><circle cx="6.5" cy="6.5" r="5" fill="none" stroke="#555" stroke-width="2"/><line x1="10" y1="10" x2="15" y2="15" stroke="#555" stroke-width="2"/></svg>
  </div>
  <nav class="abs nav">
    <ul>
      <li style="width:82px">Home</li>
      <li class="active" style="width:96px">Auctions</li>
      <li style="width:168px">Real Estate Listings</li>
      <li style="width:83px">Rentals</li>
      <li style="width:109px">Our Team</li>
      <li style="width:92px">Services</li>
      <li style="width:126px">Past Auctions</li>
      <li style="width:128px">Testimonials</li>
      <li style="width:115px">Contact Us</li>
    </ul>
  </nav>
</header>

<section>
  <div class="abs hero" role="img" aria-label="Slideshow photo: a rancher in a cowboy hat looking over a green field at dusk with power lines"></div>
  <div class="abs hero-arrow" style="left:0"><svg width="62" height="78" viewBox="0 0 62 78"><polyline points="38,22 22,39 38,56" fill="none" stroke="#fff" stroke-width="2"/></svg></div>
  <div class="abs hero-arrow" style="left:1138px"><svg width="62" height="78" viewBox="0 0 62 78"><polyline points="24,22 40,39 24,56" fill="none" stroke="#fff" stroke-width="2"/></svg></div>
  <div class="abs hero-caption serif">PELLENTESQUE ELEIFEND TORTOR JUSTO.</div>
</section>

<section>
  <h1 class="abs intro-title serif">PELLENTESQUE ELEIFEND TORTOR JUSTO, ALIQUET TRISTIQUE</h1>
  <p class="abs intro-copy">Nam molestie consectetur condimentum. Praesent dignissim ultricies arcu, ac semper magna blandit sed. Aliquam vitae porta arcu. Cras elementum semper interdum. Aliquam erat volutpat. Morbi lobortis viverra eros. Maecenas condimentum massa ut nunc bibendum venenatis. Maecenas eu nunc tellus. Nunc dapibus metus sed nunc sodales euismod.</p>
  <div class="abs divider"></div>
</section>

<main>
  <h2 class="abs section-title serif">LATEST AUCTIONS</h2>
  <div class="abs more-dot"></div>

  <article class="abs card" style="top:907px">
    <div class="photo" role="img" aria-label="Lake property with a wooden dock and trees" style="background:linear-gradient(#b9cde0,#5f8a3e 45%,#8b9a8a 70%,#6e7d6a)"></div>
    <div class="thumb" style="left:2px;background:linear-gradient(#a9c3dd,#5b6f80)" role="img" aria-label="Boathouse on the water"></div>
    <div class="thumb" style="left:133px;background:linear-gradient(#b7cde2,#6f8b52)" role="img" aria-label="Shoreline view"></div>
    <div class="thumb" style="left:263px;background:linear-gradient(#9cb8d6,#7e8f86)" role="img" aria-label="Dock over the lake"></div>
    <div class="loc"><svg width="20" height="28" viewBox="0 0 20 28"><path d="M10 0C4.5 0 0 4.5 0 10c0 7.5 10 18 10 18s10-10.5 10-18C20 4.5 15.5 0 10 0z" fill="#777"/><circle cx="10" cy="10" r="4" fill="#e6e6e6"/></svg>P.O. Box 40512, Millbrook, VA 24590</div>
    <div class="info">
      <h3>Nullam aliquet condimentum</h3>
      <p class="desc">Curabitur ipsum felis, malesuada eget volutpat ut, tristique ut ipsum. Aliquam commodo euismod fermentum. Nullam et metus sit amet lacus fringilla ornare.</p>
      <div class="sub"><p class="mode">Online Bidding Only</p>
      <p class="when"><b>Begins:</b>Tuesday, May 30, 2017 at 11:00 AM EDT<br><b>Ends:</b>Wednesday, May 31, 2017 at 11:00 AM EDT</p></div>
      <p class="mode">Live Off-Site Auction</p>
      <p class="when"><b>Begins:</b>Tuesday, May 29, 2018 at 4:00 PM EDT<br><b>Ends:</b>Wednesday, May 31, 2017 at 11:00 AM EDT</p>
    </div>
    <div class="actions">
      <span><svg width="16" height="20"><rect width="16" height="20" fill="#666"/></svg>Details</span>
      <span><svg width="20" height="16"><rect width="20" height="16" rx="2" fill="#666"/><circle cx="10" cy="8" r="4" fill="#fff"/></svg>Photos</span>
      <span><svg width="22" height="16"><rect width="22" height="16" rx="2" fill="#666"/><polygon points="8,4 15,8 8,12" fill="#fff"/></svg>Videos</span>
      <span><svg width="22" height="18"><rect width="22" height="14" rx="1" fill="#666"/><rect x="8" y="14" width="6" height="4" fill="#666"/></svg>Click here for Online Bidding</span>
    </div>
    <div class="base"></div>
  </article>

  <article class="abs card" style="top:1368px">
    <div class="photo" role="img" aria-label="White lakeside house with deck and trees" style="background:linear-gradient(#d6dde3,#8aa07a 40%,#4d6a3d 65%,#7b8f95)"></div>
    <div class="thumb" style="left:2px;background:linear-gradient(#c4d3e0,#4b6a3a)" role="img" aria-label="Trees by the water"></div>
    <div class="thumb" style="left:133px;background:linear-gradient(#d5dfe8,#5b7744)" role="img" aria-label="Lake view from lawn"></div>
    <div class="thumb" style="left:263px;background:linear-gradient(#8b7563,#4f3d33)" role="img" aria-label="Interior room"></div>
    <div class="loc"><svg width="20" height="28" viewBox="0 0 20 28"><path d="M10 0C4.5 0 0 4.5 0 10c0 7.5 10 18 10 18s10-10.5 10-18C20 4.5 15.5 0 10 0z" fill="#777"/><circle cx="10" cy="10" r="4" fill="#e6e6e6"/></svg>P.O. Box 40512, Millbrook, VA 24590</div>
    <div class="info">
      <h3>Nullam aliquet condimentum</h3>
      <p class="desc">Curabitur ipsum felis, malesuada eget volutpat ut, tristique ut ipsum. Aliquam commodo euismod fermentum. Nullam et metus sit amet lacus fringilla ornare.</p>
      <div class="sub"><p class="mode">Online Bidding Only</p>
      <p class="when"><b>Begins:</b>Tuesday, May 30, 2017 at 11:00 AM EDT<br><b>Ends:</b>Wednesday, May 31, 2017 at 11:00 AM EDT</p></div>
      <p class="mode">Live Off-Site Auction</p>
      <p class="when"><b>Begins:</b>Tuesday, May 29, 2018 at 4:00 PM EDT<br><b>Ends:</b>Wednesday, May 31, 2017 at 11:00 AM EDT</p>
    </div>
    <div class="actions">
      <span><svg width="16" height="20"><rect width="16" height="20" fill="#666"/></svg>Details</span>
      <span><svg width="20" height="16"><rect width="20" height="16" rx="2" fill="#666"/><circle cx="10" cy="8" r="4" fill="#fff"/></svg>Photos</span>
      <span><svg width="22" height="16"><rect width="22" height="16" rx="2" fill="#666"/><polygon points="8,4 15,8 8,12" fill="#fff"/></svg>Videos</span>
      <span><svg width="22" height="18"><rect width="22" height="14" rx="1" fill="#666"/><rect x="8" y="14" width="6" height="4" fill="#666"/></svg>Click here for Online Bidding</span>
    </div>
    <div class="base"></div>
  </article>

  <article class="abs card" style="top:1830px">
    <div class="photo" role="img" aria-label="Log lodge on a mountain lake reflected in the water" style="background:linear-gradient(#9fb3c6,#33502c 35%,#6b5a45 55%,#7f8f99 75%,#5d6e78)"></div>
    <div class="thumb" style="left:2px;background:linear-gradient(#4d6a3c,#7d6a50)" role="img" aria-label="Cabin in the woods"></div>
    <div class="thumb" style="left:133px;background:linear-gradient(#9fc1e0,#3f6f96)" role="img" aria-label="Boats on the lake"></div>
    <div class="thumb" style="left:263px;background:linear-gradient(#6a8a55,#8a7a66)" role="img" aria-label="Deck overlooking the lake"></div>
    <div class="loc"><svg width="20" height="28" viewBox="0 0 20 28"><path d="M10 0C4.5 0 0 4.5 0 10c0 7.5 10 18 10 18s10-10.5 10-18C20 4.5 15.5 0 10 0z" fill="#777"/><circle cx="10" cy="10" r="4" fill="#e6e6e6"/></svg>P.O. Box 40512, Millbrook, VA 24590</div>
    <div class="info">
      <h3>Nullam aliquet condimentum</h3>
      <p class="desc">Curabitur ipsum felis, malesuada eget volutpat ut, tristique ut ipsum. Aliquam commodo euismod fermentum. Nullam et metus sit amet lacus fringilla ornare.</p>
      <div class="sub"><p class="mode">Online Bidding Only</p>
      <p class="when"><b>Begins:</b>Tuesday, May 30, 2017 at 11:00 AM EDT<br><b>Ends:</b>Wednesday, May 31, 2017 at 11:00 AM EDT</p></div>
      <p class="mode">Live Off-Site Auction</p>
      <p class="when"><b>Begins:</b>Tuesday, May 29, 2018 at 4:00 PM EDT<br><b>Ends:</b>Wednesday, May 31, 2017 at 11:00 AM EDT</p>
    </div>
    <div class="actions">
      <span><svg width="16" height="20"><rect width="16" height="20" fill="#666"/></svg>Details</span>
      <span><svg width="20" height="16"><rect width="20" height="16" rx="2" fill="#666"/><circle cx="10" cy="8" r="4" fill="#fff"/></svg>Photos</span>
      <span><svg width="22" height="16"><rect width="22" height="16" rx="2" fill="#666"/><polygon points="8,4 15,8 8,12" fill="#fff"/></svg>Videos</span>
      <span><svg width="22" height="18"><rect width="22" height="14" rx="1" fill="#666"/><rect x="8" y="14" width="6" height="4" fill="#666"/></svg>Click here for Online Bidding</span>
    </div>
    <div class="base"></div>
  </article>
</main>

<aside>
  <div class="abs box notify">
    <h4>NOTIFY ME OF UPCOMING AUCTIONS</h4>
    <div class="field" style="margin-top:16px">E-mail ID</div>
    <div style="text-align:right;margin-top:8px"><span class="btn">SUBMIT</span></div>
  </div>
  <div class="abs box sell">
    <h4>I AM READY TO SELL. PLEASE CONTACT ME FOR A FREE CONSULTATION</h4>
    <svg width="28" height="18" viewBox="0 0 28 18" style="margin-top:10px"><rect width="28" height="18" fill="var(--yellow)"/><polyline points="0,0 14,10 28,0" fill="none" stroke="#3b3bcc" stroke-width="2"/></svg>
  </div>
  <div class="abs box mortgage">
    <h4><svg width="24" height="30" viewBox="0 0 24 30"><rect width="24" height="30" rx="2" fill="#fff"/><rect x="4" y="4" width="16" height="7" fill="#323232"/><g fill="#323232"><rect x="4" y="14" width="4" height="4"/><rect x="10" y="14" width="4" height="4"/><rect x="16" y="14" width="4" height="4"/><rect x="4" y="21" width="4" height="4"/><rect x="10" y="21" width="4" height="4"/><rect x="16" y="21" width="4" height="4"/></g></svg>MORTGAGE CALCULATOR</h4>
    <label>Loan Amount ($)</label><div class="field">250,000</div>
    <label>Inerest Rate (%)</label><div class="field">250,000</div>
    <label>Length of Loan (Yrs)</label><div class="field">20</div>
    <div style="text-align:right;margin-top:12px"><span class="btn">CALCULATE</span></div>
  </div>
</aside>

<section class="abs testimonials">
  <h2 class="serif">TESTIMONIALS</h2>
</section>
<svg class="abs t-arrow" style="left:40px" width="22" height="36" viewBox="0 0 22 36"><polyline points="18,3 4,18 18,33" fill="none" stroke="#888" stroke-width="2.5"/></svg>
<svg class="abs t-arrow" style="left:1138px" width="22" height="36" viewBox="0 0 22 36"><polyline points="4,3 18,18 4,33" fill="none" stroke="#888" stroke-width="2.5"/></svg>
<div class="abs avatar" role="img" aria-label="Portrait photo of the client giving the testimonial"></div>
<blockquote class="abs quote">“ Nam a malesuada libero. Duis sodales et libero vel interdum. Interdum et malesuada fames ac ante ipsum primis in faucibus. Donec lobortis dui tortor, eu lobortis felis mattis nec. Sed justo quam, luctus eu mauris eget, euismod dapibus sem. Sed tempus feugiat ante, at ornare libero volutpat sed. Maecenas quis magna magna. ”<cite>Reed Alvers, NY</cite></blockquote>

<footer>
  <div class="abs footer"></div>
  <div class="abs f-brand"><i></i>Dorlen Group</div>
  <div class="abs badge" style="left:363px;width:88px" aria-label="Association badge"></div>
  <div class="abs badge" style="left:466px;width:46px;background:#3a5fb8" aria-label="Association badge"></div>
  <div class="abs vline" style="left:564px"></div>
  <div class="abs pay" style="left:609px;background:#dcdcdc" aria-label="Payment card"></div>
  <div class="abs pay" style="left:677px;background:#e3e3e3" aria-label="Payment card"></div>
  <div class="abs pay" style="left:745px;background:#dcdcdc" aria-label="Payment card"></div>
  <div class="abs vline" style="left:856px"></div>
  <div class="abs social" style="left:901px" aria-label="Social link"></div>
  <div class="abs social" style="left:944px" aria-label="Social link"></div>
  <div class="abs social" style="left:991px" aria-label="Social link"></div>
  <div class="abs social" style="left:1036px" aria-label="Social link"></div>
  <div class="abs f-rule"></div>

  <div class="abs contact" style="left:141px"><svg width="18" height="20"><rect width="18" height="20" fill="#777"/></svg>Address: 718 N. Elm Ave., Johnson KS<br>Mailing Address: PO Box 927, Johnson, KS</div>
  <div class="abs contact" style="left:495px;top:2713px"><svg width="20" height="20" viewBox="0 0 20 20" style="top:0"><path d="M4 1l4 4-2 3c1 2 4 5 6 6l3-2 4 4-3 3C9 19 1 11 1 4z" fill="#777"/></svg>Phone: (555) 318-7061</div>
  <div class="abs contact" style="left:743px;top:2713px"><svg width="20" height="20" style="top:0"><rect y="6" width="20" height="14" fill="#777"/><rect x="4" width="12" height="8" fill="#999"/></svg>Fax : (555) 318-7095</div>
  <div class="abs contact" style="left:946px;top:2713px"><svg width="22" height="15" style="top:3px"><rect width="22" height="15" fill="#777"/><polyline points="0,0 11,8 22,0" fill="none" stroke="#2b2b2b" stroke-width="1.5"/></svg>E-mail : dgroup@vrbx.com</div>

  <div class="abs copyright">Copyright © 2014 Dorlen Group. All rights reserved.</div>
</footer>

</body>
</html>
```